Stationery and Business Card Design

We need stationary design for our new company pelvanta. Pelvanta is a company that provides city apartment rentals for tourists in Athens We need business cards, letterheads for A4 and A5 and envelopes for A4 A5. The design needs to be modern, friendly and corporate.

Target Market(s)

City Tourists

Industry/Entity Type

Tourism

```html
<!DOCTYPE html>
<html lang="en">
<head>
<meta charset="utf-8">
<title>Pelvanta Apartments – Stationery</title>
<link rel="stylesheet" href="https://fonts.googleapis.com/css2?family=Raleway:wght@400;500&display=swap">
<style>
  :root {
    --plum: #7b1e4f;
    --charcoal: #434343;
    --backdrop: #d2d1d3;
    --paper: #f3f3f3;
    --envelope: #fafafa;
    --grey-text: #555555;
  }
  * { margin: 0; padding: 0; box-sizing: border-box; }
  html, body { width: 1200px; height: 991px; overflow: hidden; }
  body {
    background: var(--backdrop);
    font-family: "Raleway", sans-serif;
    position: relative;
  }
  .envelope {
    position: absolute;
    background: var(--envelope);
  }
  .envelope-flap { position: absolute; left: 0; top: 0; width: 100%; }
  .flap-shape { fill: var(--plum); }
  .flap-mark { fill: #ffffff; }

  .envelope--large { left: 154px; top: 107px; width: 483px; height: 683px; }
  .envelope--small { left: 773px; top: 330px; width: 334px; height: 476px; }

  .sheet {
    position: absolute;
    display: flex;
    flex-direction: column;
    background: var(--paper);
  }
  .sheet-head {
    display: flex;
    flex-direction: column;
    align-items: center;
  }
  .brand-square { background: var(--plum); }
  .brand-name {
    color: var(--plum);
    font-weight: 400;
    line-height: 1;
    letter-spacing: -0.02em;
  }
  .brand-tagline {
    display: flex;
    align-items: center;
    color: var(--plum);
    font-weight: 500;
    text-transform: uppercase;
  }
  .brand-tagline::before,
  .brand-tagline::after {
    content: "";
    display: block;
    height: 1px;
    background: var(--grey-text);
  }
  .sheet-band { background: var(--plum); }
  .sheet-foot {
    background: var(--charcoal);
    color: #ffffff;
    text-align: center;
    display: flex;
    flex-direction: column;
    align-items: center;
  }

  /* large sheet */
  .sheet--large { left: 92px; top: 202px; width: 482px; height: 682px; }
  .sheet--large .sheet-head { height: 230px; padding-top: 64px; }
  .sheet--large .brand-square { width: 54px; height: 55px; }
  .sheet--large .brand-name { font-size: 36px; margin-top: 9px; }
  .sheet--large .brand-tagline { font-size: 9px; letter-spacing: 0.32em; margin-top: 3px; gap: 8px; }
  .sheet--large .brand-tagline::before,
  .sheet--large .brand-tagline::after { width: 30px; }
  .sheet--large .sheet-band { height: 349px; }
  .sheet--large .sheet-foot { height: 103px; padding-top: 43px; font-size: 7.5px; line-height: 10px; }

  /* small sheet */
  .sheet--small { left: 717px; top: 402px; width: 341px; height: 482px; }
  .sheet--small .sheet-head { height: 164px; padding-top: 48px; }
  .sheet--small .brand-square { width: 38px; height: 38px; }
  .sheet--small .brand-name { font-size: 26px; margin-top: 7px; }
  .sheet--small .brand-tagline { font-size: 6.5px; letter-spacing: 0.32em; margin-top: 2px; gap: 6px; }
  .sheet--small .brand-tagline::before,
  .sheet--small .brand-tagline::after { width: 22px; }
  .sheet--small .sheet-band { height: 246px; }
  .sheet--small .sheet-foot { height: 72px; padding-top: 31px; font-size: 5px; line-height: 6.5px; }
</style>
</head>
<body>

  <div class="envelope envelope--large">
    <svg class="envelope-flap" width="483" height="70" viewBox="0 0 483 70">
      <polygon class="flap-shape" points="0,0 483,0 466,69 18,69"/>
      <rect class="flap-mark" x="226" y="21" width="31" height="31"/>
    </svg>
  </div>

  <section class="sheet sheet--large">
    <header class="sheet-head">
      <div class="brand-square"></div>
      <div class="brand-name">Pelvanta</div>
      <div class="brand-tagline">Apartments</div>
    </header>
    <div class="sheet-band"></div>
    <footer class="sheet-foot">
      <span>14 Irodou Attikou St</span>
      <span>Athens, GR, 10674</span>
    </footer>
  </section>

  <div class="envelope envelope--small">
    <svg class="envelope-flap" width="334" height="48" viewBox="0 0 334 48">
      <polygon class="flap-shape" points="0,0 334,0 321,48 11,48"/>
      <rect class="flap-mark" x="156" y="14" width="22" height="22"/>
    </svg>
  </div>

  <section class="sheet sheet--small">
    <header class="sheet-head">
      <div class="brand-square"></div>
      <div class="brand-name">Pelvanta</div>
      <div class="brand-tagline">Apartments</div>
    </header>
    <div class="sheet-band"></div>
    <footer class="sheet-foot">
      <span>14 Irodou Attikou St</span>
      <span>Athens, GR, 10674</span>
    </footer>
  </section>

</body>
</html>
```